Scrap Metal Recycling

We are looking for a simple yet bold business card. We already have the logo, please see attached. Color scheme of blue, black and white or just blue and white.

```html
<!DOCTYPE html>
<html lang="en">
<head>
<meta charset="utf-8">
<title>Harbor Alloy Co. – Business Card</title>
<link href="https://fonts.googleapis.com/css2?family=Montserrat:wght@400;500;700&display=swap" rel="stylesheet">
<style>
  :root {
    --stage: #3b3b3b;
    --card: #1a1a1b;
    --card-back: #141415;
    --pattern: #232324;
    --blue: #1b8fc0;
    --white: #f4f4f4;
  }
  * { box-sizing: border-box; margin: 0; padding: 0; }
  html, body { width: 1200px; height: 801px; overflow: hidden; }
  body {
    background: var(--stage);
    font-family: "Montserrat", Arial, sans-serif;
    color: var(--white);
    position: relative;
  }
  .card {
    position: absolute;
    top: 246px;
    width: 540px;
    height: 309px;
    background: var(--card);
    border-bottom: 3px solid var(--blue);
    border-left: 2px solid var(--blue);
    overflow: hidden;
  }
  .card--front { left: 40px; }
  .card--back { left: 620px; background: var(--card-back); }

  /* Front */
  .identity {
    position: absolute; right: 34px; top: 34px; text-align: right;
  }
  .identity__name {
    color: var(--blue); font-weight: 700; font-size: 21px; letter-spacing: -0.3px;
  }
  .identity__role { font-size: 13px; margin-top: 2px; }
  .identity__rule {
    width: 200px; height: 1px; background: var(--blue); margin: 10px 0 10px auto;
  }
  .identity__address { font-size: 13px; line-height: 1.45; }

  .brand {
    position: absolute; left: 34px; top: 120px;
  }
  .brand__name {
    display: flex; align-items: center; gap: 10px;
    font-weight: 700; font-size: 26px; color: var(--white); letter-spacing: 0.5px;
  }
  .brand__dot { width: 14px; height: 14px; border-radius: 50%; background: var(--blue); }
  .brand__tagline {
    color: var(--blue); font-size: 11px; letter-spacing: 4.5px; margin-top: 6px; font-weight: 500;
  }

  .divider {
    position: absolute; left: 34px; right: 34px; top: 214px; height: 1px; background: var(--blue);
  }
  .contacts {
    position: absolute; left: 34px; top: 226px; list-style: none;
    font-size: 13px; line-height: 22px;
  }
  .contacts li { display: flex; align-items: center; gap: 9px; }
  .contacts svg { width: 12px; height: 12px; fill: var(--blue); flex: none; }

  /* Back */
  .back-pattern {
    position: absolute; inset: 0;
    background: linear-gradient(135deg, var(--card-back) 0%, var(--pattern) 100%);
  }
  .back-brand {
    position: absolute; inset: 0; display: flex; align-items: center; justify-content: center; gap: 10px;
    font-weight: 700; font-size: 22px; color: var(--white); letter-spacing: 0.5px;
  }
</style>
</head>
<body>
  <section class="card card--front">
    <div class="identity">
      <div class="identity__name">MARCUS VALE</div>
      <div class="identity__role">President</div>
      <div class="identity__rule"></div>
      <div class="identity__address">1820 Quayside Drive<br>Seacliff CA 90412</div>
    </div>

    <div class="brand">
      <div class="brand__name"><span>HARBOR ALLOY CO.</span><span class="brand__dot"></span></div>
      <div class="brand__tagline">SCRAP METAL RECYCLING</div>
    </div>

    <div class="divider"></div>

    <ul class="contacts">
      <li>
        <svg viewBox="0 0 24 24" aria-hidden="true"><path d="M6.6 10.8a15.1 15.1 0 0 0 6.6 6.6l2.2-2.2a1 1 0 0 1 1-.25 11.4 11.4 0 0 0 3.6.57 1 1 0 0 1 1 1V20a1 1 0 0 1-1 1A17 17 0 0 1 3 4a1 1 0 0 1 1-1h3.5a1 1 0 0 1 1 1c0 1.25.2 2.45.57 3.57a1 1 0 0 1-.25 1z"/></svg>
        555-310-4872
      </li>
      <li>
        <svg viewBox="0 0 24 24" aria-hidden="true"><path d="M2 5h20v14H2zm2 2v.5l8 5 8-5V7l-8 5z"/></svg>
        marcus@harboralloy.com
      </li>
      <li>
        <svg viewBox="0 0 24 24" aria-hidden="true"><circle cx="12" cy="12" r="10"/></svg>
        www.harboralloy.com
      </li>
    </ul>
  </section>

  <section class="card card--back">
    <div class="back-pattern" role="img" aria-label="Tonal repeating pattern of the company mark on black"></div>
    <div class="back-brand"><span>HARBOR ALLOY CO.</span></div>
  </section>
</body>
</html>
```